Pell School of Dental Assisting needs a WP (re)design.

We need a colorful Wordpress design for a relaunch of an old website. The relaunch is already underway and the website is live. The home page URL is brindlecrestacademy.example I have just completed a ArtFlock logo and the new logo is live on the website also. The installed Wordpress theme that is being used is Loomer III Plus with their "Talvek" subtheme. I would like a (re)design using the colors that are currently being represented by the new logo, and any additional complimentary colors. The information regarding the business can be found on the website already, so please review it for insight. The name of the business is "R. Jon Pell School of Dental Assisting".

Target Market(s)

The targeted website viewer is an adult female between the ages of 18 and 30 who is interested in attending our short term 10 week career school. The targeted audience's perception is two fold. Number one, they must have or develop interest in a future healthcare career and number two, they must complete the necessary requirements of our 10 week training course.

This website should inspire in the target viewer both the benefits of dental assistant employment and the essential learning and skills training required. Many of these potential student candidates are desperately wanting to get a job with income.

In addition to the hope of future employment, the website must represent the schools objectives are, classroom education and hands on clinical trainingl. Each webpage must represent both of these meanings to the targeted potential student.

Industry/Entity Type

Business

Font styles to use
Sans Serif

Requirements
Must have
• The phone number placed in a visible and high value widget area that allows mobile phone browser dialing.

```html
<!DOCTYPE html>
<html lang="en">
<head>
<meta charset="utf-8">
<title>Pell School of Dental Assisting</title>
<link href="https://fonts.googleapis.com/css2?family=Open+Sans:wght@400;600&family=PT+Sans:wght@400;700&display=swap" rel="stylesheet">
<style>
:root{
  --accent:#3aaee6;
  --navy:#2d4c9c;
  --band:#4b8ea8;
  --footer:#232323;
  --footer-line:#3a3a3a;
  --text:#555;
  --heading:#222;
  --muted:#999;
  --rule:#e3e3e3;
}
*{box-sizing:border-box;margin:0;padding:0}
html,body{width:878px;height:1200px;overflow:hidden;background:#fff}
body{position:relative;font-family:"PT Sans",sans-serif;color:var(--text)}
.abs{position:absolute}
.logo{left:165px;top:22px;font:400 20px "Open Sans",sans-serif;color:#333}
.nav{left:360px;top:22px;display:flex;align-items:center;gap:2px;list-style:none}
.nav li{font:400 8px "Open Sans",sans-serif;letter-spacing:.3px;color:#666;padding:7px 8px}
.nav li.active{background:var(--accent);color:#fff}
.nav .search{padding:0 8px}
.hero{left:0;top:68px;width:878px;height:368px;background:linear-gradient(180deg,#6fa9cf 0%,#8dbbd8 55%,#3c86b5 75%,#5da0c8 100%)}
.hero-person{left:440px;top:68px;width:438px;height:368px;background:radial-gradient(ellipse at 60% 40%,#e9d8cc 0%,#cdb3a0 35%,rgba(120,90,70,.6) 60%,rgba(120,160,200,0) 80%)}
.hero-title{left:165px;top:196px;color:#fff;font:600 26px/1.1 "Open Sans",sans-serif}
.hero-title .big{font-size:31px}
.hero-sub{left:165px;top:275px;color:#fff;font:400 17px/1.4 "Open Sans",sans-serif}
.hero-call{left:167px;top:340px;width:172px;height:28px;background:rgba(35,60,80,.45);color:#fff;font:400 17px/28px "Open Sans",sans-serif;padding-left:5px;text-decoration:none}
.slider{left:165px;top:398px;width:538px;height:1px;background:rgba(255,255,255,.85)}
.slide-num{top:400px;color:#fff;font:600 7px "Open Sans",sans-serif}
.section-title{font:400 10px "PT Sans",sans-serif;color:#333}
.section-title::after{content:"";display:block;width:24px;height:2px;background:var(--accent);margin-top:6px}
.badge{height:15px;font:400 6px/15px "Open Sans",sans-serif;color:#fff;text-align:center}
.badge.date{background:var(--navy);width:44px}
.badge.count{background:var(--accent);width:15px}
.photo{background:linear-gradient(160deg,#7f9f6a,#cfd7c5 60%,#f2f2f2)}
.post-title{font:700 13px/1.15 "PT Sans",sans-serif;color:var(--heading);width:168px}
.post-text{font:400 7px/9.6px "Open Sans",sans-serif;color:#666;width:168px}
.acc-head{left:531px;top:486px;width:182px;height:20px;background:var(--navy);color:#fff;font:400 7px/20px "Open Sans",sans-serif;padding-left:6px}
.acc-head .minus{position:absolute;right:6px;top:9px;width:8px;height:2px;background:#fff}
.acc-thumb{left:531px;top:518px;width:42px;height:46px;background:linear-gradient(160deg,#6d8fb3,#e3e3e3)}
.acc-text{left:581px;top:518px;width:132px;font:400 6.5px/9.5px "Open Sans",sans-serif;color:#777}
.btn-details{left:672px;top:572px;width:41px;height:15px;background:var(--navy);color:#fff;font:400 7px/15px "Open Sans",sans-serif;text-align:center}
.acc-item{left:531px;width:182px;height:23px;border-bottom:1px solid var(--rule);font:400 7px/23px "Open Sans",sans-serif;color:var(--navy)}
.acc-item .plus{position:absolute;right:3px;top:6px}
.testi{left:531px;top:776px;width:182px;height:128px;border:1px solid #cfcfcf;padding:16px 18px 0 19px;font:400 7px/10.5px "Open Sans",sans-serif;color:#666}
.testi .author{position:absolute;right:22px;top:98px;color:var(--navy)}
.newsletter{left:0;top:928px;width:878px;height:38px;background:var(--band)}
.nl-label{left:167px;top:940px;color:#fff;font:400 12px "PT Sans",sans-serif}
.nl-input{top:938px;width:126px;height:18px;background:#dde7ec;font:400 7px/18px "Open Sans",sans-serif;color:#888;padding-left:5px}
.nl-btn{left:663px;top:938px;width:50px;height:18px;background:#fff;color:#222;font:600 7px/18px "Open Sans",sans-serif;text-align:center}
.footer{left:0;top:966px;width:878px;height:234px;background:var(--footer)}
.f-title{font:400 10px "PT Sans",sans-serif;color:#fff}
.f-title::after{content:"";display:block;width:24px;height:2px;background:var(--accent);margin-top:6px}
.f-text{font:400 6.5px/10px "Open Sans",sans-serif;color:#9a9a9a;width:170px}
.f-arrows{display:flex;gap:3px}
.f-arrows span{width:14px;height:14px;border:1px solid #555;display:flex;align-items:center;justify-content:center}
.f-list{list-style:none;width:172px}
.f-list li{position:relative;padding-left:10px;font:400 6.5px/9px "Open Sans",sans-serif;color:#ddd;margin-bottom:8px}
.f-list li::before{content:"\2192";position:absolute;left:0;top:0;color:#fff}
.f-list .when{display:block;color:var(--accent)}
.social{left:168px;top:1112px;display:flex;gap:8px}
.social span{width:12px;height:12px;background:#555}
.f-rule{left:165px;top:1176px;width:548px;height:1px;background:var(--footer-line)}
.copy{left:165px;top:1184px;font:400 6.5px "Open Sans",sans-serif;color:#aaa}
.top{left:693px;top:1184px;font:400 6.5px "Open Sans",sans-serif;color:#aaa}
</style>
</head>
<body>

<header>
  <div class="abs logo">Logo</div>
  <ul class="abs nav">
    <li class="active">HOME</li><li>ABOUT US</li><li>INFORMATION</li><li>BLOG</li><li>RESOURCES</li><li>CONTACT US</li>
    <li class="search"><svg width="8" height="8" viewBox="0 0 10 10"><circle cx="4" cy="4" r="3" fill="none" stroke="#777" stroke-width="1.3"/><line x1="6.2" y1="6.2" x2="9.2" y2="9.2" stroke="#777" stroke-width="1.3"/></svg></li>
  </ul>
</header>

<section>
  <div class="abs hero" role="img" aria-label="Smiling young woman raising her arms against a blue sky and sea"></div>
  <div class="abs hero-person" aria-hidden="true"></div>
  <h1 class="abs hero-title">Learn How to Become<br><span class="big">A Dental Assistant</span></h1>
  <p class="abs hero-sub">In just 10 Weeks on Saturdays Only – 50% Classroom<br>and 50% Hands On Clinical Training</p>
  <a class="abs hero-call" href="tel:5550134720">Call (555) 013-4720</a>
  <div class="abs slider"></div>
  <span class="abs slide-num" style="left:166px">1</span>
  <span class="abs slide-num" style="left:348px">2</span>
  <span class="abs slide-num" style="left:530px">3</span>
</section>

<main>
  <h2 class="abs section-title" style="left:165px;top:452px">Latest News</h2>

  <div class="abs badge date" style="left:165px;top:488px">12 DEC 12</div>
  <div class="abs badge count" style="left:211px;top:488px">2</div>
  <div class="abs photo" style="left:165px;top:520px;width:168px;height:104px" role="img" aria-label="Portrait of a smiling dentist in a white coat"></div>
  <h3 class="abs post-title" style="left:165px;top:639px">Lorem ipsum dolor sit amat velum</h3>
  <p class="abs post-text" style="left:165px;top:677px">Lorem ipsum dolor sit amet, consectetur adipiscing elit. Ut volutpat rutrum eros sit amet sollicitudin. Suspendisse pulvinar, velit nec pharetra interdum, ante tellus ornare mi, et mollis tellus neque vitae elit. Mauris adipiscing mauris.</p>

  <div class="abs badge date" style="left:348px;top:488px">12 DEC 12</div>
  <div class="abs badge count" style="left:394px;top:488px">3</div>
  <div class="abs photo" style="left:348px;top:520px;width:168px;height:104px" role="img" aria-label="Portrait of a smiling instructor outdoors"></div>
  <h3 class="abs post-title" style="left:348px;top:639px">Lorem ipsum dolor sit amat velum</h3>
  <p class="abs post-text" style="left:348px;top:677px">Lorem ipsum dolor sit amet, consectetur adipiscing elit. Ut volutpat rutrum eros sit amet sollicitudin. Suspendisse pulvinar, velit nec pharetra interdum, ante tellus ornare mi, et mollis tellus neque vitae elit. Mauris adipiscing mauris.</p>

  <h2 class="abs section-title" style="left:531px;top:452px">Pages</h2>
  <div class="abs acc-head">About R. Jon Pell School of Dental Assisting<span class="minus"></span></div>
  <div class="abs acc-thumb" role="img" aria-label="Portrait of the school director"></div>
  <p class="abs acc-text">Mauris adipiscing fringilla turpis interd tellus ornare etos polim. Pulvinar est cardio neque vitae elit. Lorem vulputat pontra nunc gravida.</p>
  <div class="abs btn-details">Details</div>
  <div class="abs acc-item" style="top:600px">Dental Assistant Resources<svg class="plus" width="10" height="10" viewBox="0 0 10 10"><path d="M5 0v10M0 5h10" stroke="#2d4c9c" stroke-width="1"/></svg></div>
  <div class="abs acc-item" style="top:623px">Dental Assistant School Information<svg class="plus" width="10" height="10" viewBox="0 0 10 10"><path d="M5 0v10M0 5h10" stroke="#2d4c9c" stroke-width="1"/></svg></div>
  <div class="abs acc-item" style="top:646px">Contact R. Jon Pell School of Dental Assisting<svg class="plus" width="10" height="10" viewBox="0 0 10 10"><path d="M5 0v10M0 5h10" stroke="#2d4c9c" stroke-width="1"/></svg></div>
  <div class="abs acc-item" style="top:669px;border-bottom:none">R. Jon Pell School of Dental Assisting<svg class="plus" width="10" height="10" viewBox="0 0 10 10"><path d="M5 0v10M0 5h10" stroke="#2d4c9c" stroke-width="1"/></svg></div>

  <h2 class="abs section-title" style="left:165px;top:749px">View our portfolia</h2>
  <div class="abs" style="left:165px;top:777px;width:168px;height:127px;background:linear-gradient(150deg,#9bb68c,#e9e4de 50%,#c9d6e0)" role="img" aria-label="Dentist examining a patient in the clinic chair"></div>
  <div class="abs" style="left:348px;top:777px;width:168px;height:127px;background:linear-gradient(160deg,#f3f3f6,#d9dbe6 60%,#c05a62)" role="img" aria-label="Close-up of a bright smile with a dental mirror"></div>

  <h2 class="abs section-title" style="left:531px;top:749px">Tesmonials</h2>
  <div class="abs testi">Lorem ipsum dolor sit amet, consectetuer adipiscing elit. Aenean commodo ligula eget dolor. Aenean massa. Cum sociis natoque penatibus et magnis dis parturient montes, nascetur ridiculus mus. Donec quam felis, ultricies nec, pellentesque eu, pretium quis, sem. Nulla consequat massa
    <span class="author">-Marlowe</span></div>
</main>

<section>
  <div class="abs newsletter"></div>
  <div class="abs nl-label">Subscribe to our Newsletter</div>
  <div class="abs nl-input" style="left:348px">Enter Your Name</div>
  <div class="abs nl-input" style="left:492px">Enter Your Email</div>
  <div class="abs nl-btn">SIGN UP</div>
</section>

<footer>
  <div class="abs footer"></div>
  <h2 class="abs f-title" style="left:165px;top:990px">Pell School of Dental Assisting</h2>
  <p class="abs f-text" style="left:165px;top:1020px">R. Jon Pell School of Dental Assisting is Certified by the State Workforce Board Career Schools and Colleges</p>
  <p class="abs f-text" style="left:165px;top:1055px">R. Jon Pell School of Dental Assisting Harbor Medical Center 4820 Meadow Loop, Ste 310 Cedar Falls, TX 70000 (555) 013-4720</p>
  <div class="abs social"><span></span><span></span><span></span><span></span></div>

  <h2 class="abs f-title" style="left:348px;top:990px">Latest Posts</h2>
  <div class="abs f-arrows" style="left:481px;top:991px">
    <span><svg width="7" height="5" viewBox="0 0 7 5"><path d="M7 2.5H1M3 .5L1 2.5 3 4.5" stroke="#fff" fill="none" stroke-width=".8"/></svg></span>
    <span><svg width="7" height="5" viewBox="0 0 7 5"><path d="M0 2.5h6M4 .5l2 2-2 2" stroke="#fff" fill="none" stroke-width=".8"/></svg></span>
  </div>
  <ul class="abs f-list" style="left:348px;top:1020px">
    <li>Mauris adipiscing mauris fringilla turpis interdum sed pulvinar nisi malesuada<span class="when">3 years ago</span></li>
    <li>Lorem ipsum dolor sit amat velum<span class="when">3 years ago</span></li>
    <li>Mauris adipiscing mauris fringilla turpis interdum sed pulvinar nisi malesuada<span class="when">3 years ago</span></li>
  </ul>

  <h2 class="abs f-title" style="left:531px;top:990px">Latest Tweets</h2>
  <div class="abs f-arrows" style="left:681px;top:991px">
    <span><svg width="7" height="5" viewBox="0 0 7 5"><path d="M7 2.5H1M3 .5L1 2.5 3 4.5" stroke="#fff" fill="none" stroke-width=".8"/></svg></span>
    <span><svg width="7" height="5" viewBox="0 0 7 5"><path d="M0 2.5h6M4 .5l2 2-2 2" stroke="#fff" fill="none" stroke-width=".8"/></svg></span>
  </div>
  <ul class="abs f-list" style="left:531px;top:1020px">
    <li>New version 3.5 of FitHaus - Responsive Gym Fitness Theme is available: lnk.example/a7Qw2<span class="when">about 23 hours ago</span></li>
    <li>Tidal Pricing Grid Kit updated to v4.1 - lnk.example/k3Rt8<span class="when">6 days ago</span></li>
    <li>New version 3.0 of Drift Box has been released. Please check update info: lnk.example/p9Lm4<span class="when">14 days ago</span></li>
  </ul>

  <div class="abs f-rule"></div>
  <div class="abs copy">© Copyright · Pell School. All rights reserved</div>
  <div class="abs top">Top <svg width="6" height="7" viewBox="0 0 6 7"><path d="M3 7V1M1 3l2-2 2 2" stroke="#fff" fill="none" stroke-width="1"/></svg></div>
</footer>

</body>
</html>
```